Kitchen and custom cabinetry company looking for business card design

We make: * Custom Kitchens, contemporary and traditional kitchens, Vanities, Libraries, Custom Entry Doors, Custom Wine Cellars and Custom Design Furniture. Phone number 555-318-2746. Address: Westhampton NY. Email: BRAVOK@mailbox.example Portfolio at: BRAVOKcabinetry.example I would like moderns fonts and not heavy lines. double side but maybe will use clear plastic. I attached the logo.

```html
<!DOCTYPE html>
<html lang="en">
<head>
<meta charset="utf-8">
<title>Bravok Cabinetry Inc. – Business Card</title>
<link rel="stylesheet" href="https://fonts.googleapis.com/css2?family=Marcellus&display=swap">
<style>
  :root {
    --orange: #f15a29;
    --grey: #808080;
    --white: #ffffff;
    --backdrop: #e8e4de;
    --card-w: 409px;
    --card-h: 715px;
  }
  * { margin: 0; padding: 0; box-sizing: border-box; }
  html, body {
    width: 1200px;
    height: 970px;
    overflow: hidden;
    background: var(--backdrop);
    font-family: "Marcellus", serif;
  }
  .canvas { position: relative; width: 1200px; height: 970px; }

  .card {
    position: absolute;
    top: 129px;
    width: var(--card-w);
    height: var(--card-h);
    border-radius: 23px;
    overflow: hidden;
    background: var(--white);
  }
  .card--front { left: 167px; --accent: var(--orange); --stripe: var(--grey); }
  .card--back  { left: 626px; --accent: var(--grey);   --stripe: var(--orange); }

  .card__cap     { position: absolute; left: 0; top: 0; width: 100%; height: 30px; background: var(--accent); }
  .card__stripe  { position: absolute; left: 0; width: 100%; background: var(--stripe); }
  .card__stripe--upper { top: 297px; height: 26px; }
  .card__stripe--lower { top: 371px; height: 23px; }
  .card__panel   { position: absolute; left: 0; top: 394px; width: 100%; height: 321px; background: var(--accent); }

  .brand {
    position: absolute;
    left: 0; top: 138px;
    width: 100%;
    display: flex;
    align-items: center;
    justify-content: center;
    gap: 12px;
  }
  .brand__mark { width: 18px; height: 18px; background: var(--orange); }
  .brand__name {
    font-size: 24px;
    letter-spacing: 2px;
    color: var(--grey);
    text-transform: uppercase;
  }

  .info {
    position: absolute;
    left: 0; width: 100%;
    text-align: center;
    color: var(--white);
    line-height: 1;
  }
  .info p { position: absolute; left: 0; width: 100%; font-size: 16px; }
  .info .name { top: 455px; font-size: 20px; font-weight: 700; letter-spacing: 0.5px; }
  .info .role { top: 478px; font-size: 15px; }
  .info .addr1 { top: 520px; }
  .info .addr2 { top: 541px; }
  .info .phone { top: 597px; }
  .info .email { top: 617px; }
  .info .web   { top: 638px; }

  .specialties__title {
    position: absolute; left: 0; top: 477px; width: 100%;
    text-align: center; color: var(--white);
    font-size: 21px; font-weight: 700; letter-spacing: 0.5px; line-height: 1;
  }
  .specialties__list {
    position: absolute; left: 0; top: 522px; width: 100%;
    list-style: none; text-align: center; color: var(--white);
    font-size: 16px; line-height: 20.4px; letter-spacing: 0.3px;
  }
</style>
</head>
<body>
<div class="canvas">

  <section class="card card--front" aria-label="Business card front">
    <div class="card__cap"></div>
    <div class="brand">
      <span class="brand__mark"></span>
      <span class="brand__name">Bravok Cabinetry Inc.</span>
    </div>
    <div class="card__stripe card__stripe--upper"></div>
    <div class="card__stripe card__stripe--lower"></div>
    <div class="card__panel"></div>
    <div class="info">
      <p class="name">Marco Delgado</p>
      <p class="role">Owner</p>
      <p class="addr1">2290 Harbor Mill rd,</p>
      <p class="addr2">Eastport, NY, 11900</p>
      <p class="phone">555-318-2746</p>
      <p class="email">BRAVOK@mailbox.example</p>
      <p class="web">www.BRAVOKcabinetry.example</p>
    </div>
  </section>

  <section class="card card--back" aria-label="Business card back">
    <div class="card__cap"></div>
    <div class="brand">
      <span class="brand__mark"></span>
      <span class="brand__name">Bravok Cabinetry Inc.</span>
    </div>
    <div class="card__stripe card__stripe--upper"></div>
    <div class="card__stripe card__stripe--lower"></div>
    <div class="card__panel"></div>
    <h2 class="specialties__title">OUR SPECIALTIES</h2>
    <ul class="specialties__list">
      <li>CONTEMPORAY KITCHENS</li>
      <li>TRADITIONAL KITCHENS</li>
      <li>VANITIES</li>
      <li>LIBRARIES</li>
      <li>CUSTOM WINE CELLARS</li>
      <li>CUSTOM DESIGN FURNITURE</li>
    </ul>
  </section>

</div>
</body>
</html>
```